Emergency Medical Training and Events Company Business Needs Business Card Design

We are in need of a business card for our dynamic company expanding its customer base and need to be easily contacted and identified for when we visit with government officials, potential EMS / Fire agencies and county coordinators to arrange for training programs for first responders to better prepare them for critical thinking at critical incidents.

Target Market(s)

EMS/Fire and Event Promoters

Industry/Entity Type

Medical

Contact Information for Business Card

Two cards, comparable designs:

Martin K. Halvey, Principal, m.halvey@rvqtlo.com
Owen Tash, Event and Training Specialist, o.tash@rvqtlo.com

Font styles to use
Other font styles liked:
• Cambria

Colors

Designer to choose colors to be used in the design.

Requirements
Must have
• Company Logo, Spots for Name, Title, Phone Number, Email, Website
• A bullet list stating that we offer, QRB CPR and First Aid Instructors, Hold the Line Instructors, Event EMS, CME's, MCI Training and Planning. We prefer to have a black background for the card but if you can make a blue or white card stand out we would review that as well.
Should not have
• Tacky logos or special sayings ... simple, elegant, professional is the look we seek

```html
<!DOCTYPE html>
<html lang="en">
<head>
<meta charset="utf-8">
<title>R.V.Q. Solutions – Business Cards</title>
<link href="https://fonts.googleapis.com/css2?family=Caladea:wght@400;700&display=swap" rel="stylesheet">
<style>
  :root {
    --navy: #000f61;
    --red: #d20605;
    --white: #ffffff;
    --page: #ffffff;
  }
  html, body {
    margin: 0;
    padding: 0;
    width: 1200px;
    height: 1200px;
    overflow: hidden;
    background: var(--page);
  }
  .sheet {
    position: relative;
    width: 1200px;
    height: 1200px;
  }
  .card {
    position: absolute;
    width: 436px;
    height: 262px;
    display: block;
  }
  .card--front-top { left: 147px; top: 283px; }
  .card--back-top  { left: 625px; top: 282px; }
  .card--front-bottom { left: 147px; top: 668px; }
  .card--back-bottom  { left: 625px; top: 666px; }

  .shared-defs { position: absolute; width: 0; height: 0; overflow: hidden; }

  .fill-navy { fill: var(--navy); }
  .fill-red { fill: var(--red); }
  .fill-white { fill: var(--white); }
  .line-navy { fill: none; stroke: var(--navy); stroke-width: 3; }
  .icon-stroke { fill: none; stroke: var(--navy); stroke-width: 2.2; stroke-linecap: round; stroke-linejoin: round; }

  .brand-name {
    font-family: "Caladea", "Cambria", serif;
    font-weight: 700;
    fill: var(--white);
  }
  .contact-text {
    font-family: "Caladea", "Cambria", serif;
    font-weight: 400;
    font-size: 22px;
    fill: var(--white);
  }
  .person-name {
    font-family: "Caladea", "Cambria", serif;
    font-weight: 700;
    fill: var(--white);
  }
  .person-title {
    font-family: "Caladea", "Cambria", serif;
    font-weight: 400;
    fill: var(--white);
  }
  .person-title--spaced { letter-spacing: 7px; font-size: 15px; }
  .person-title--plain { font-size: 14px; }
</style>
</head>
<body>
<svg class="shared-defs" aria-hidden="true">
  <defs>
    <g id="front-face">
      <rect class="fill-navy" x="0" y="0" width="697" height="419"/>
      <!-- corner stripes -->
      <polygon class="fill-red" points="0,78 78,0 127,0 0,127"/>
      <polygon class="fill-red" points="0,293 126,419 77,419 0,342"/>
      <!-- chevron flowing into the band -->
      <polygon class="fill-red" points="203,0 252,0 397,145 697,145 697,274 397,274 252,419 203,419 400,222 Q 412,209.5 400,197 Z"/>
      <!-- brand mark -->
      <circle class="fill-white" cx="67" cy="207" r="52"/>
      <rect class="fill-red" x="130" y="168" width="2" height="78"/>
      <text class="brand-name" x="145" y="205" font-size="46">R.V.Q.</text>
      <text class="brand-name" x="145" y="243" font-size="30">Solutions</text>
    </g>

    <g id="back-face">
      <rect class="fill-navy" x="0" y="0" width="697" height="419"/>
      <!-- corner triangles -->
      <polygon class="fill-red" points="0,0 41,0 0,41"/>
      <polygon class="fill-red" points="697,0 656,0 697,41"/>
      <polygon class="fill-red" points="0,419 41,419 0,378"/>
      <polygon class="fill-red" points="697,419 656,419 697,378"/>
      <!-- top V -->
      <polygon class="fill-red" points="183,0 238,0 348,110 458,0 513,0 348,165"/>
      <polyline class="line-navy" points="226,18 348,140 470,18"/>
      <!-- bottom V -->
      <polygon class="fill-red" points="183,419 348,253 513,419 458,419 348,309 238,419"/>
      <polyline class="line-navy" points="226,401 348,279 470,401"/>

      <!-- contact icons -->
      <g transform="translate(19,103)">
        <rect class="fill-white" width="29" height="29" rx="5"/>
        <rect class="icon-stroke" x="10" y="6" width="9" height="16" rx="1.5"/>
        <circle class="fill-navy" cx="14.5" cy="19" r="1"/>
      </g>
      <g transform="translate(19,163)">
        <rect class="fill-white" width="29" height="29" rx="5"/>
        <path class="icon-stroke" d="M8 7 L11 7 L13 11 L11 13 Q13 17 16 18 L18 16 L22 18 L22 21 Q20 23 17 22 Q9 19 7 10 Q7 8 8 7 Z"/>
        <path class="icon-stroke" d="M17 7 Q21 8 22 12"/>
      </g>
      <g transform="translate(19,227)">
        <rect class="fill-white" width="29" height="29" rx="5"/>
        <circle class="icon-stroke" cx="14.5" cy="14.5" r="8"/>
        <ellipse class="icon-stroke" cx="14.5" cy="14.5" rx="3.5" ry="8"/>
        <line class="icon-stroke" x1="6.5" y1="14.5" x2="22.5" y2="14.5"/>
      </g>
      <g transform="translate(19,288)">
        <rect class="fill-white" width="29" height="29" rx="5"/>
        <rect class="icon-stroke" x="7" y="9" width="15" height="11" rx="1"/>
        <polyline class="icon-stroke" points="7,10 14.5,16 22,10"/>
      </g>

      <text class="contact-text" x="63" y="125">555.014.2002</text>
      <text class="contact-text" x="63" y="185">555.017.7890</text>
      <text class="contact-text" x="68" y="247">www.rvqtlo.com</text>
    </g>
  </defs>
</svg>

<main class="sheet">
  <svg class="card card--front-top" viewBox="0 0 697 419" role="img" aria-label="Card front, R.V.Q. Solutions">
    <use href="#front-face"/>
  </svg>

  <svg class="card card--back-top" viewBox="0 0 697 419" role="img" aria-label="Card back, Martin K. Halvey">
    <use href="#back-face"/>
    <text class="contact-text" x="70" y="308">m.halvey@rvqtlo.com</text>
    <text class="person-name" x="678" y="213" font-size="35" text-anchor="end">Martin K. Halvey</text>
    <text class="person-title person-title--spaced" x="556" y="231" text-anchor="middle">PRINCIPAL</text>
  </svg>

  <svg class="card card--front-bottom" viewBox="0 0 697 419" role="img" aria-label="Card front, R.V.Q. Solutions">
    <use href="#front-face"/>
  </svg>

  <svg class="card card--back-bottom" viewBox="0 0 697 419" role="img" aria-label="Card back, Owen Tash">
    <use href="#back-face"/>
    <text class="contact-text" x="70" y="308">o.tash@rvqtlo.com</text>
    <text class="person-name" x="675" y="213" font-size="40" text-anchor="end">Owen Tash</text>
    <text class="person-title person-title--plain" x="572" y="230" text-anchor="middle">Event and Training Specialist</text>
  </svg>
</main>
</body>
</html>
```